Belmora Wines

Hi all,

My name’s Tom Welling and I run a small wine brand based in the Canberra Wine District, Australia. I’m currently in the process of branding the business and am looking for a designer to help develop a new visual direction.

Background
I’ll be growing my own fruit from a leased vineyard site Named 'Ashbrook' and my family’s property named 'Tallin Park', with a stronger emphasis on organic practices and site expression.

The Direction
The brand will centre around single vineyard wines, with each wine reflecting the unique site it comes from. I’d like the branding to support this idea of place, origin, and authenticity.

In terms of visual style, I’m drawn to something that is:

Simple and effective
A balance between traditional and modern
Clean, considered, and not overly decorative

Nothing too over-the-top, the goal is something timeless that lets the wine and vineyard story speak for itself.

At this stage, I’m mainly looking for:

Conceptual design direction / ideas
Label design (with potential to expand into broader branding)

I’m open to creative interpretation, so if the story resonates with you, I’d love to see how you would approach it.

Below I've attached an example of the bottle shape I will be using.

Cheers,
Tom

Colors
0054AA
0677BA
7BADD7
CADEEF
E8F1F8
FFC000
F8CF3A
FAE287
FDF2CF
FEFAEE

Requirements
Must have
• Mix of modern and traditional

```html
<!DOCTYPE html>
<html lang="en">
<head>
<meta charset="utf-8">
<title>Belmora Wines — Riesling Label</title>
<link rel="stylesheet" href="https://fonts.googleapis.com/css2?family=Marcellus&family=Questrial&family=Lato:wght@700&family=Cormorant+Garamond:wght@400&display=swap">
<style>
  :root {
    --backdrop: #f7f4f0;
    --label-cream: #fdfbf7;
    --label-peach: #fdebd2;
    --ink: #2b2925;
    --ink-soft: #5a5854;
    --ink-faint: #b9b5ae;
    --vine-light: rgba(214, 229, 138, 0.85);
    --vine-mid: rgba(156, 196, 60, 0.9);
    --vine-deep: rgba(79, 138, 42, 0.85);
    --vine-clear: rgba(214, 229, 138, 0);
  }
  * { margin: 0; padding: 0; box-sizing: border-box; }
  html, body {
    width: 802px;
    height: 1200px;
    overflow: hidden;
    background: var(--backdrop);
  }
  .label {
    position: absolute;
    left: 51px;
    top: 236px;
    width: 700px;
    height: 728px;
    background: linear-gradient(90deg, var(--label-cream) 0%, var(--label-cream) 55%, var(--label-peach) 100%);
    box-shadow: 0 2px 10px rgba(0,0,0,0.06);
  }
  .vintage {
    position: absolute;
    left: 588px;
    top: 40px;
    width: 72px;
    font-family: "Questrial", sans-serif;
    font-size: 28px;
    line-height: 30px;
    letter-spacing: 9px;
    text-align: center;
    color: var(--ink);
  }
  .vineyard-art {
    position: absolute;
    left: 179px;
    top: 153px;
    width: 368px;
    height: 204px;
    background:
      radial-gradient(closest-side at 72% 50%, var(--vine-deep) 0%, rgba(79,138,42,0.35) 55%, rgba(79,138,42,0) 100%) 0 0 / 100% 100% no-repeat,
      radial-gradient(closest-side at 50% 50%, var(--vine-mid) 0%, var(--vine-light) 45%, var(--vine-clear) 100%) 0 0 / 100% 100% no-repeat;
  }
  .brand {
    position: absolute;
    left: 0;
    width: 100%;
    top: 386px;
    text-align: center;
    font-family: "Marcellus", serif;
    font-weight: 400;
    font-size: 92px;
    line-height: 92px;
    letter-spacing: 5px;
    color: var(--ink);
    padding-left: 20px;
  }
  .region {
    position: absolute;
    left: 0;
    width: 100%;
    top: 487px;
    text-align: center;
    font-family: "Questrial", sans-serif;
    font-size: 25px;
    letter-spacing: 4.5px;
    color: var(--ink-soft);
    padding-left: 20px;
  }
  .varietal {
    position: absolute;
    left: 0;
    width: 100%;
    top: 556px;
    text-align: center;
    font-family: "Lato", sans-serif;
    font-weight: 700;
    font-size: 40px;
    letter-spacing: 5px;
    color: var(--ink);
  }
  .country {
    position: absolute;
    left: 0;
    width: 100%;
    top: 634px;
    text-align: center;
    font-family: "Cormorant Garamond", serif;
    font-size: 32px;
    letter-spacing: 17px;
    color: var(--ink-soft);
    padding-left: 8px;
  }
  .specs {
    position: absolute;
    left: 144px;
    width: 412px;
    top: 676px;
    display: flex;
    align-items: center;
    font-family: "Cormorant Garamond", serif;
    font-size: 21px;
    color: var(--ink-faint);
  }
  .specs .rule {
    flex: 1;
    height: 1px;
    background: var(--ink-faint);
    margin: 0 6px;
  }
</style>
</head>
<body>
  <main class="label">
    <div class="vintage">20<br>19</div>
    <div class="vineyard-art" role="img" aria-label="Sketched illustration of vineyard rows with cypress trees"></div>
    <h1 class="brand">BELMORA</h1>
    <p class="region">CANBERRA WINE DISTRICT</p>
    <h2 class="varietal">RIESLING</h2>
    <p class="country">AUSTRALIA</p>
    <div class="specs">
      <span class="alc">13.5% ALC</span>
      <span class="rule"></span>
      <span class="volume">750 ML</span>
    </div>
  </main>
</body>
</html>
```